Brochure required for large legal practice

We require a brochure, poster and PowerPoint to be designed to promote our new Employee Benefits Program to our employees. The brochure needs to be modern, clean and corporate. Our target market is solicitors, legal support staff and administration staff based across multiple sites in Queensland, Australia. Logos and brochure/poster content have been attached as well as a detailed brief.

Please note that several photos of our employees have now been uploaded and can be used in this material only.                             

Legal

```html
<!DOCTYPE html>
<html lang="en">
<head>
<meta charset="utf-8">
<title>About us – Harwell Group Employee Benefits Program</title>
<link rel="stylesheet" href="https://fonts.googleapis.com/css2?family=Poppins:ital,wght@0,400;0,600;1,300;1,400&display=swap">
<style>
  :root {
    --ink: #111111;
    --band: #000000;
    --paper-light: #ffffff;
    --paper-edge: #c9c9c9;
    --logo-grey: #6f6f6f;
    --photo-warm: #c9a98c;
    --photo-cool: #8e98a3;
  }
  * { margin: 0; padding: 0; box-sizing: border-box; }
  html, body { width: 848px; height: 1200px; overflow: hidden; }
  body {
    font-family: "Poppins", "Century Gothic", sans-serif;
    color: var(--ink);
    background: var(--paper-light);
  }
  .page {
    position: relative;
    width: 848px;
    height: 1200px;
    background: linear-gradient(90deg, var(--paper-edge) 0%, var(--paper-light) 28%, var(--paper-light) 72%, var(--paper-edge) 100%);
    overflow: hidden;
  }
  .title-band {
    position: absolute;
    left: 0; top: 92px;
    width: 848px; height: 44px;
    z-index: 1;
  }
  .title-band svg { position: absolute; left: 0; top: 0; }
  .page-title {
    position: absolute;
    z-index: 2;
    left: 118px; top: 86px;
    font-style: italic;
    font-weight: 400;
    font-size: 44px;
    line-height: 54px;
    letter-spacing: -1px;
    white-space: nowrap;
    color: var(--ink);
  }
  .intro {
    position: absolute;
    left: 140px; top: 152px;
    width: 568px;
    font-style: italic;
    font-weight: 300;
    font-size: 14.6px;
    line-height: 18.6px;
    text-align: justify;
  }
  .intro p { margin-bottom: 18.6px; }
  .team-photo {
    position: absolute;
    left: 275px; top: 836px;
    width: 302px; height: 207px;
    background: linear-gradient(120deg, var(--photo-warm) 0%, #e6ddd3 45%, var(--photo-cool) 100%);
    box-shadow: 0 2px 6px rgba(0,0,0,0.25);
  }
  .brand {
    position: absolute;
    left: 0; top: 1084px;
    width: 848px;
    display: flex;
    justify-content: center;
    align-items: center;
    gap: 12px;
  }
  .brand-mark {
    width: 26px; height: 26px;
    background: var(--logo-grey);
  }
  .brand-name {
    font-weight: 600;
    font-size: 26px;
    color: var(--logo-grey);
    letter-spacing: 0.5px;
  }
  .web-address {
    position: absolute;
    left: 0; top: 1140px;
    width: 848px;
    text-align: center;
    font-weight: 600;
    font-size: 17px;
    color: var(--ink);
  }
</style>
</head>
<body>
  <main class="page">
    <div class="title-band" aria-hidden="true">
      <svg width="848" height="44" viewBox="0 0 848 44">
        <polygon points="0,0 112,0 100,44 0,44" fill="var(--band)"/>
        <polygon points="326,0 848,0 848,44 314,44" fill="var(--band)"/>
      </svg>
    </div>
    <h1 class="page-title">About us</h1>

    <section class="intro">
      <p>Welcome to the Harwell Group Employee Benefits Program.</p>
      <p>Harwell Group aims to foster a relaxed and warm culture emphasising teamwork and the celebration of achievement.</p>
      <p>We value our employees and have, therefore, designed an Employee Benefits Program to both express thanks and reward our people for their ongoing loyalty and dedication.</p>
      <p>Our Employee Benefits program also follows our belief that everyone benefits from a healthy work/life balance in order to continue to grow and prosper both professionally and personally.</p>
      <p>The program contains a wide range of benefits including health initiatives, financial savings, social events and activities, shopping and travel discounts as well as rewards for length of service and contribution.</p>
      <p>Employees of Harwell Group and its subsidiaries (“Employees”) who have successfully completed their probationary period and who are employed on a permanent or long term casual basis are eligible to take part in our Employee Benefits Program.</p>
      <p>For more information, please see the terms and conditions for each item, or see a member of the Human Resources team.</p>
      <p>Terms and conditions are accurate as at the time of going to print, but since the availability of these benefits is determined by our affiliated service providers, we cannot guarantee that any of the benefits will be offered on a long-term basis. From time to time, any of the benefits currently advertised may change without prior warning, and some may be discontinued altogether. Whilst we have no control over these changes, we will notify Employees as they come to our attention.</p>
    </section>

    <div class="team-photo" role="img" aria-label="Photo of a smiling employee holding a pen in an office, with colleagues working in the background"></div>

    <div class="brand">
      <span class="brand-mark" aria-hidden="true"></span>
      <span class="brand-name">Harwell Group</span>
    </div>
    <p class="web-address">www.harwelllaw.com</p>
  </main>
</body>
</html>
```